Wool Product Label / Yarn Band

Looking to update the packaging on our wool products. This includes a design for a paper band to place around braided wool or yarn, and a design for a sticker to place on the outside of tissue paper wrapping. Open to updating or modifying the logo, which does not fit well on a round sticker, but the sticker could also be something wool related (like a sheep or drop spindle) that does not include the logo.
Target Market(s)
Wool crafters (knitters / spinners / felters). Mainly women, aged 30-70
Industry/Entity Type
Textile
Colors
Designer to choose colors to be used in the design.
Requirements
Must have
- Band needs to include, brand name, logo, url (fernloomstead.com), dyelot number, as well as the fiber content (ex: Merino Wool) and weight of the fiber (ex: 4oz).
Nice to have
- Band would ideally be easily customized because the weight and fiber content is variable and will be printed specifically for each product, Variable information can be on a sticker or printed directly on a band that can be printed on a standard printer. Attached is a photo of the current band and it's application.

```html
<!DOCTYPE html>
<html lang="en">
<head>
<meta charset="utf-8">
<title>Fernloomstead yarn band options</title>
<link href="https://fonts.googleapis.com/css2?family=Roboto+Condensed:wght@400;700&family=Arimo:ital,wght@0,400;1,700&family=Michroma&display=swap" rel="stylesheet">
<style>
:root{
  --paper:#ffffff;
  --ink:#1e1e1e;
  --brand-green:#4ba93b;
  --tag-grey:#5a5a5a;
  --url-blue:#2b2f8c;
  --rose:#c9505e;
  --rose-soft:#f7c9cf;
  --lime:#b8dc80;
  --charcoal:#24261f;
  --olive-gold:#c7c77a;
  --leaf:#9cbf45;
  --stamp-green:#0f4f2f;
  --stamp-green-2:#176b3f;
  --gold-1:#f6eab8;
  --gold-2:#d8bf72;
  --gold-3:#b99847;
  --globe:#1f6fb8;
}
*{margin:0;padding:0;box-sizing:border-box}
html,body{width:1091px;height:1200px;overflow:hidden;background:var(--paper)}
.canvas{position:relative;width:1091px;height:1200px;background:var(--paper);font-family:"Arimo",Arial,sans-serif;color:var(--ink)}
.abs{position:absolute}
.center{transform:translateX(-50%);white-space:nowrap;text-align:center}

/* dimensions */
.dim-line{position:absolute;background:var(--rose)}
.dim-label{position:absolute;font:700 17px "Arimo",Arial,sans-serif;color:var(--ink);white-space:nowrap}

/* shared type */
.brand-name{font-family:"Roboto Condensed","Arial Narrow",sans-serif;font-weight:700;color:var(--brand-green);letter-spacing:-1px;line-height:1}
.tagline{font-family:"Roboto Condensed","Arial Narrow",sans-serif;font-weight:400;line-height:1}
.spec{font-family:"Arimo",Arial,sans-serif;line-height:1}
.url{font-family:"Michroma","Arial",sans-serif;letter-spacing:3px;line-height:1;white-space:nowrap}
.globe{position:absolute;border-radius:50%;background:var(--globe);border:2px solid #cfe3f5}

/* band 1 */
.band-rose{left:59px;top:134px;width:925px;height:300px;background:var(--paper);border:1px solid var(--rose)}
.pattern{position:absolute;top:12px;width:209px;height:277px;background:linear-gradient(135deg,#fbd6da,var(--rose-soft) 50%,#f2b5bd)}
.flourish{position:absolute;border-radius:50%;background:linear-gradient(90deg,#f3b6be,var(--rose),#f3b6be)}

/* band 2 */
.band-noir{left:59px;top:468px;width:926px;height:299px;background:var(--lime)}
.laurel{position:absolute;border-radius:40%;background:var(--leaf);opacity:.85}
.scroll-ornament{position:absolute;border-radius:50%;background:linear-gradient(90deg,transparent,var(--olive-gold),transparent)}

/* band 3 */
.band-stamp{left:63px;top:812px;width:919px;height:287px;background:
  repeating-linear-gradient(0deg,var(--stamp-green) 0 3px,var(--stamp-green-2) 3px 5px)}
.perf{position:absolute;left:0;right:0;height:10px;background:radial-gradient(circle,var(--paper) 3.2px,transparent 3.8px) 0 0/10px 10px repeat-x}
.perf.v{top:0;bottom:0;width:10px;height:auto;left:auto;right:auto;background-repeat:repeat-y}
.gold-frame{position:absolute;left:20px;top:13px;width:879px;height:259px;border:3px solid var(--gold-2)}
.gold-band{position:absolute;left:46px;top:61px;width:825px;height:164px;
  background:repeating-linear-gradient(0deg,rgba(255,255,255,.18) 0 2px,transparent 2px 5px),
  linear-gradient(90deg,var(--gold-2),var(--gold-1) 30%,var(--gold-1) 70%,var(--gold-2));
  border-left:10px solid #1b1b14;border-right:10px solid #1b1b14}
.gold-oval{position:absolute;left:250px;top:34px;width:420px;height:218px;border-radius:50%;
  background:radial-gradient(ellipse at center,var(--gold-1),var(--gold-2) 80%,var(--gold-3));
  border:3px solid var(--stamp-green-2)}
.stamp-spec{font-family:"Arimo",Arial,sans-serif;font-style:italic;font-weight:700;color:#1a1a12;line-height:1.25}
</style>
</head>
<body>
<main class="canvas">

  <!-- size marks -->
  <div class="dim-line" style="left:59px;top:100px;width:1px;height:34px"></div>
  <div class="dim-line" style="left:984px;top:104px;width:1px;height:30px"></div>
  <div class="dim-line" style="left:59px;top:119px;width:355px;height:1px"></div>
  <div class="dim-line" style="left:628px;top:119px;width:356px;height:1px"></div>
  <div class="dim-label" style="left:522px;top:109px;transform:translateX(-50%)">8.5 inch</div>
  <div class="dim-line" style="left:984px;top:134px;width:52px;height:1px"></div>
  <div class="dim-line" style="left:984px;top:434px;width:52px;height:1px"></div>
  <div class="dim-line" style="left:1013px;top:134px;width:1px;height:100px"></div>
  <div class="dim-line" style="left:1013px;top:336px;width:1px;height:98px"></div>
  <div class="dim-label" style="left:1013px;top:284px;transform:translate(-50%,-50%) rotate(-90deg)">2.75 inch</div>

  <!-- band 1: rose lattice -->
  <section class="abs band-rose" aria-label="Rose lattice yarn band">
    <div class="pattern" style="left:10px" role="img" aria-label="Pink quatrefoil lattice pattern"></div>
    <div class="pattern" style="right:10px" role="img" aria-label="Pink quatrefoil lattice pattern"></div>
    <svg class="abs" style="left:0;top:0" width="925" height="300" viewBox="0 0 925 300">
      <path d="M232 21H693V33H705V45C770 55 804 100 804 150C804 200 770 245 705 255V267H693V279H232V267H220V255C155 245 115 200 115 150C115 100 155 55 220 45V33H232Z" fill="#fff" stroke="#fff" stroke-width="22"/>
      <path d="M232 21H693V33H705V45C770 55 804 100 804 150C804 200 770 245 705 255V267H693V279H232V267H220V255C155 245 115 200 115 150C115 100 155 55 220 45V33H232Z" fill="#fff" stroke="var(--rose)" stroke-width="2.5"/>
      <path d="M236 26H689V37H700V49C762 59 798 102 798 150C798 198 762 241 700 251V263H689V274H236V263H225V251C163 241 121 198 121 150C121 102 163 59 225 49V37H236Z" fill="none" stroke="var(--rose)" stroke-width="1"/>
    </svg>
    <div class="flourish" style="left:401px;top:28px;width:120px;height:14px" role="img" aria-label="Red scroll ornament"></div>
    <div class="abs center brand-name" style="left:461px;top:50px;font-size:50px">fernloomstead</div>
    <div class="abs center tagline" style="left:496px;top:146px;font-size:20px;color:var(--tag-grey)">hand painted yarn &amp; fibers</div>
    <div class="abs center spec" style="left:457px;top:188px;font-size:23px">85% Merino Wool / Dyelot No: 00</div>
    <div class="abs center spec" style="left:457px;top:213px;font-size:23px">Qty: 4.0 oz</div>
    <div class="globe" style="left:250px;top:247px;width:22px;height:22px"></div>
    <div class="abs url" style="left:278px;top:250px;font-size:16px;color:var(--url-blue)">WWW.FERNLOOMSTEAD.COM</div>
  </section>

  <!-- band 2: charcoal & olive -->
  <section class="abs band-noir" aria-label="Charcoal yarn band">
    <svg class="abs" style="left:0;top:0" width="926" height="299" viewBox="0 0 926 299">
      <path d="M125 10H800V28H818V42C880 60 859 100 859 150C859 200 880 238 818 256V270H800V289H125V270H107V256C45 238 66 200 66 150C66 100 45 60 107 42V28H125Z" fill="var(--charcoal)"/>
      <path d="M140 30H785V44H800V58C840 72 838 110 838 150C838 190 840 228 800 242V256H785V270H140V256H125V242C85 228 87 190 87 150C87 110 85 72 125 58V44H140Z" fill="none" stroke="var(--olive-gold)" stroke-width="1.5"/>
      <path d="M147 36H778V49H793V62C830 76 832 112 832 150C832 188 830 224 793 238V251H778V264H147V251H132V238C95 224 93 188 93 150C93 112 95 76 132 62V49H147Z" fill="none" stroke="var(--olive-gold)" stroke-width=".8"/>
    </svg>
    <div class="laurel" style="left:116px;top:98px;width:22px;height:104px" role="img" aria-label="Laurel sprig ornament"></div>
    <div class="laurel" style="left:788px;top:98px;width:22px;height:104px" role="img" aria-label="Laurel sprig ornament"></div>
    <div class="abs center brand-name" style="left:463px;top:45px;font-size:52px">fernloomstead</div>
    <div class="abs center tagline" style="left:500px;top:123px;font-size:21px;color:#fff">hand painted yarn &amp; fibers</div>
    <div class="abs center spec" style="left:463px;top:161px;font-size:24px;color:#fff">85% Merino Wool / Dyelot No: 00</div>
    <div class="abs center spec" style="left:463px;top:186px;font-size:24px;color:#fff">Qty: 4.0 oz</div>
    <div class="scroll-ornament" style="left:339px;top:215px;width:250px;height:16px" role="img" aria-label="Olive scroll ornament"></div>
    <div class="globe" style="left:206px;top:237px;width:26px;height:26px"></div>
    <div class="abs url" style="left:241px;top:241px;font-size:19px;color:#e6efc2">WWW.FERNLOOMSTEAD.COM</div>
  </section>

  <!-- band 3: green stamp with gold -->
  <section class="abs band-stamp" aria-label="Green and gold stamp yarn band">
    <div class="perf" style="top:-5px"></div>
    <div class="perf" style="bottom:-5px"></div>
    <div class="perf v" style="left:-5px"></div>
    <div class="perf v" style="right:-5px"></div>
    <div class="gold-frame"></div>
    <div class="gold-band"></div>
    <div class="gold-oval"></div>
    <div class="laurel" style="left:385px;top:50px;width:150px;height:16px;border-radius:50%" role="img" aria-label="Laurel arc ornament"></div>
    <div class="laurel" style="left:385px;top:220px;width:150px;height:16px;border-radius:50%" role="img" aria-label="Laurel arc ornament"></div>
    <div class="abs center brand-name" style="left:460px;top:92px;font-size:52px">fernloomstead</div>
    <div class="abs center tagline" style="left:472px;top:166px;font-size:20px;color:#fff">hand painted yarn &amp; fibers</div>
    <div class="abs stamp-spec" style="left:92px;top:132px;font-size:18px">Qty: 4.0 oz</div>
    <div class="abs stamp-spec center" style="left:770px;top:124px;font-size:17px">85% Merino Wool<br>Dyelot No: 00</div>
    <div class="abs url" style="left:64px;top:210px;font-size:8.5px;letter-spacing:1px;color:#1a1a12">WWW.FERNLOOMSTEAD.COM</div>
  </section>

</main>
</body>
</html>
```